Business card

would like a double sided business card made up with my logos provided.
Prefer card to have black background and to use the black logos, with matching blue writing for the text.
One side to just be the logo, (Try to use both the black logos)
the other side to have the logo and also my credentials/business information.

Covering all aspects of Carpentry and Building Services

Marcus Thelwin
Qualified Carpenter
Mob: 0417263985
Email: rkt.joinery@fernmail.example
ABN: 47 619 283 504

Industry/Entity Type

Business

Contact Information for Business Card

Marcus Thelwin
Qualified Carpenter
Mob: 0417263985
ABN: 47 619 283 504

Requirements
Must have
• Please try to use both the black logos and incorporate into the card.

```html
<!DOCTYPE html>
<html lang="en">
<head>
<meta charset="utf-8">
<title>RKT Joinery – Business Card</title>
<link rel="stylesheet" href="https://fonts.googleapis.com/css2?family=Open+Sans:wght@400;600;700&display=swap">
<style>
  :root {
    --canvas: #e9e7e4;
    --card-dark: #2a2b2e;
    --card-dark-edge: #1c1d1f;
    --card-light: #ffffff;
    --ink: #3b3c3e;
    --ink-soft: #222325;
    --accent: #2aa3dc;
    --accent-deep: #1f6fb8;
    --ghost: #f1f2f4;
    --on-dark: #ffffff;
  }
  * { box-sizing: border-box; margin: 0; padding: 0; }
  html, body { width: 1200px; height: 800px; overflow: hidden; }
  body {
    background: var(--canvas);
    font-family: "Open Sans", Arial, sans-serif;
    position: relative;
  }
  .card {
    position: absolute;
    width: 540px;
    height: 315px;
    top: 242px;
    overflow: hidden;
    box-shadow: 0 6px 18px rgba(0,0,0,.18);
  }

  /* Back side */
  .card--back {
    left: 40px;
    background: radial-gradient(ellipse at 45% 40%, #3a3b3f 0%, var(--card-dark) 55%, var(--card-dark-edge) 100%);
    color: var(--on-dark);
  }
  .back__brand {
    position: absolute;
    left: 0; right: 0; top: 96px;
    display: flex; align-items: center; justify-content: center; gap: 16px;
  }
  .brand-mark {
    width: 30px; height: 30px;
    background: var(--accent);
  }
  .back__name {
    font-weight: 600;
    font-size: 50px;
    letter-spacing: 2px;
    color: var(--on-dark);
  }
  .back__tagline {
    position: absolute;
    left: 0; right: 0; bottom: 34px;
    text-align: center;
    font-size: 16px;
    color: var(--on-dark);
  }

  /* Front side */
  .card--front {
    left: 620px;
    background: var(--card-light);
    color: var(--ink);
  }
  .front__ghost {
    position: absolute;
    right: -20px; bottom: -36px;
    font-weight: 600;
    font-size: 150px;
    color: var(--ghost);
    letter-spacing: 4px;
  }
  .front__brand {
    position: absolute;
    right: 34px; top: 34px;
    display: flex; align-items: center; gap: 12px;
  }
  .front__brand .brand-mark { width: 24px; height: 24px; }
  .front__name {
    font-weight: 600;
    font-size: 40px;
    letter-spacing: 1px;
    color: var(--ink);
  }
  .person {
    position: absolute;
    left: 34px; top: 134px;
  }
  .person__name {
    font-weight: 700;
    font-size: 22px;
    color: var(--ink);
  }
  .person__role {
    font-size: 14px;
    color: var(--accent);
  }
  .contact {
    position: absolute;
    left: 250px; top: 136px;
    padding-left: 16px;
    border-left: 3px solid var(--accent);
  }
  .contact__row {
    display: flex; align-items: center; gap: 8px;
    font-size: 14px;
    color: var(--ink-soft);
    line-height: 24px;
  }
  .contact__icon { width: 16px; height: 16px; flex: none; }
  .abn {
    position: absolute;
    left: 34px; top: 232px;
    font-size: 17px;
    color: var(--ink-soft);
  }
</style>
</head>
<body>

  <section class="card card--back" aria-label="Business card, back">
    <div class="back__brand">
      <span class="brand-mark" aria-hidden="true"></span>
      <span class="back__name">RKT Joinery</span>
    </div>
    <p class="back__tagline">Covering all aspects of Carpentry and Building Services</p>
  </section>

  <section class="card card--front" aria-label="Business card, front">
    <span class="front__ghost" aria-hidden="true">RKT</span>
    <div class="front__brand">
      <span class="brand-mark" aria-hidden="true"></span>
      <span class="front__name">RKT Joinery</span>
    </div>

    <div class="person">
      <p class="person__name">Marcus Thelwin</p>
      <p class="person__role">Qualified Carpenter</p>
    </div>

    <div class="contact">
      <p class="contact__row">
        <svg class="contact__icon" viewBox="0 0 16 16" aria-hidden="true">
          <rect x="3" y="0.5" width="10" height="15" rx="2" fill="var(--accent)"/>
          <rect x="5" y="2.5" width="6" height="9" fill="#fff"/>
          <circle cx="8" cy="13.4" r="1" fill="#fff"/>
        </svg>
        0417263985
      </p>
      <p class="contact__row">
        <svg class="contact__icon" viewBox="0 0 16 16" aria-hidden="true">
          <rect x="0.5" y="3" width="15" height="10" rx="1" fill="var(--accent)"/>
          <path d="M1 3.6 L8 9 L15 3.6" fill="none" stroke="#fff" stroke-width="1.3"/>
        </svg>
        rkt.joinery@fernmail.example
      </p>
    </div>

    <p class="abn">ABN: 47 619 283 504</p>
  </section>

</body>
</html>
```